Упаковка для Bright Vega
Задание на дизайн
Приоритеты объектов в упаковке
Зонтичная марка, Знак производителя, Марка продукта, Вид продукта, Название продукта, Иллюстрация
Размеры
Опишите свою организацию или продукт и целевую аудиторию
Производство и продажа электро-, бензо-, аккумуляторного инструмента для строительства и ремонта.
Существующая упаковка .То, что хочется обновить.
Образец существующей упаковки.
Комментарии и пожелания для дизайнеров
Необходимо полностью обновить устаревший дизайн упаковки для инструмента, на примере шуруповерта. Фирменный красный цвет, а также сам логотип и сочетания цветов внутри него менять нельзя. Логотип обязательно должен присутствовать на упаковке. Название серии Zet power line должно остаться, но в любом другом виде и написании. Остальное можно менять до неузнаваемости. Фото инструмента должно быть помещено на упаковку целиком. Упаковка должна быть современной, сочной, красочной, информативной и обязательно несложно адаптивной под другие виды инструмента и форматы коробок (ушм, перфораторы, лобзики и пр.). Другие образцы наших упаковок можно легко найти в сети.

```html
<!DOCTYPE html>
<html lang="ru">
<head>
<meta charset="utf-8">
<title>Bright Vega — дрель, упаковка</title>
<link rel="stylesheet" href="https://fonts.googleapis.com/css2?family=Russo+One&family=Exo+2:wght@600;700&display=swap">
<style>
  :root {
    --brand-red: #b1272b;
    --accent-orange: #e2561f;
    --text-white: #ffffff;
    --page-bg: #ffffff;
    --photo-dark: #2a2426;
    --photo-red: #c0282e;
  }
  html, body {
    margin: 0;
    width: 1200px;
    height: 675px;
    overflow: hidden;
    background: var(--page-bg);
  }
  .pack-front {
    position: absolute;
    left: 240px;
    top: 38px;
    width: 720px;
    height: 598px;
    background: var(--brand-red);
    overflow: hidden;
    color: var(--text-white);
    font-family: "Russo One", "Arial Black", sans-serif;
  }
  .accent-band { position: absolute; inset: 0; }
  .brand-name {
    position: absolute;
    left: 144px;
    top: 108px;
    margin: 0;
    font-size: 40px;
    line-height: 1;
    font-weight: 400;
  }
  .kit-count {
    position: absolute;
    left: 460px;
    top: 88px;
    display: flex;
    align-items: center;
    gap: 10px;
  }
  .kit-count__number { font-size: 46px; line-height: 1; }
  .kit-count__label { font-size: 15px; line-height: 1.05; }
  .product-type {
    position: absolute;
    left: 144px;
    top: 192px;
    margin: 0;
    font-size: 70px;
    line-height: 1;
    font-weight: 400;
  }
  .product-features {
    position: absolute;
    left: 146px;
    top: 286px;
    margin: 0;
    font-size: 20px;
    line-height: 1.05;
  }
  .product-spec {
    position: absolute;
    left: 146px;
    top: 360px;
    margin: 0;
    font-size: 34px;
    line-height: 1;
  }
  .series-name {
    position: absolute;
    left: 146px;
    top: 432px;
    font-family: "Exo 2", "Arial", sans-serif;
    font-weight: 700;
  }
  .series-name__main { display: block; font-size: 36px; line-height: 1.02; }
  .series-name__sub {
    display: block;
    font-size: 17px;
    font-weight: 600;
    letter-spacing: 8px;
    margin-top: 4px;
  }
  .tool-photo {
    position: absolute;
    left: 462px;
    top: 140px;
    width: 205px;
    height: 390px;
    border-radius: 14px;
    background: linear-gradient(180deg, var(--photo-dark) 0%, var(--photo-red) 55%, var(--photo-dark) 100%);
  }
  .brand-name--large {
    position: absolute;
    left: 400px;
    top: 428px;
    font-size: 50px;
    line-height: 1;
  }
</style>
</head>
<body>
  <main class="pack-front">
    <svg class="accent-band" width="720" height="598" viewBox="0 0 720 598" aria-hidden="true">
      <polygon fill="var(--accent-orange)" points="0,320 0,250 215,120 720,300 720,375 215,195"/>
    </svg>

    <p class="brand-name">Bright Vega</p>

    <div class="kit-count">
      <span class="kit-count__number">118</span>
      <span class="kit-count__label">АКСЕССУАРОВ<br>В КОМПЛЕКТЕ</span>
    </div>

    <h1 class="product-type">ДРЕЛЬ</h1>
    <p class="product-features">БЕСЩЕТОЧНАЯ<br>АККУМУЛЯТОРНАЯ</p>
    <p class="product-spec">20V/2.0Ah</p>

    <div class="series-name">
      <span class="series-name__main">ZET</span>
      <span class="series-name__main">POWER</span>
      <span class="series-name__sub">LINE</span>
    </div>

    <div class="tool-photo" role="img" aria-label="Фото аккумуляторной бесщеточной дрели с батареей, целиком"></div>

    <p class="brand-name--large">Bright Vega</p>
  </main>
</body>
</html>
```